Visitenkarten-Design für Baubetreuung/Bauplanung/Baufinanzierung
Zielgruppe
Baubetreuung einfach gemacht! Von der Planung, Auswahl des richtigen Hausbaupartners, über die Finanzierung, bis hin zur Baubegleitung während des Baus und der Übergabe, begleiten wir den Kunden und stellen Entscheidungshilfen zur Auswahl.
Aufgabenstellung
Slogan: Einfach Kinderleicht bauen
Das Kinderleichte bauen soll widergespiegelt werden, so dass der Kunde gleich das Gefühl hat, dass er uns sorglos sein Bauvorhaben anvertrauen kann. Gleichzeitig soll die Visitenkarte Vertrauen erwecken und Qualität widerspiegeln.

```html
<!DOCTYPE html>
<html lang="de">
<head>
<meta charset="utf-8">
<title>HAUSKLAR.DE – Visitenkarte</title>
<link href="https://fonts.googleapis.com/css2?family=Montserrat:wght@400;500;600;700&display=swap" rel="stylesheet">
<style>
  :root {
    --teal: #5fc0d6;
    --ink: #1f2a30;
    --paper: #f5f5f5;
    --paper-edge: #e9e9e9;
    --rule: #b9bfc2;
    --white: #ffffff;
    --canvas: #ffffff;
  }
  * { margin: 0; padding: 0; box-sizing: border-box; }
  html, body { width: 1200px; height: 1200px; overflow: hidden; background: var(--canvas); }
  body { position: relative; font-family: "Montserrat", sans-serif; color: var(--ink); }

  .card {
    position: absolute;
    top: 451px;
    width: 540px;
    height: 297px;
    overflow: hidden;
  }
  .card--front { left: 40px; background: var(--teal); }
  .card--back {
    left: 620px;
    background: linear-gradient(135deg, var(--white) 0%, var(--paper) 55%, var(--paper-edge) 100%);
  }

  /* front */
  .edge-notch {
    position: absolute;
    top: 108px;
    width: 5px;
    height: 82px;
    background: var(--white);
  }
  .edge-notch--left { left: 6px; }
  .edge-notch--right { right: 6px; }

  .brand-name {
    font-weight: 600;
    letter-spacing: 0.5px;
    color: var(--ink);
    line-height: 1;
    white-space: nowrap;
  }
  .front-brand {
    position: absolute;
    left: 0; right: 0;
    top: 126px;
    text-align: center;
  }
  .front-brand .brand-name { font-size: 31px; }

  .front-web {
    position: absolute;
    left: 0; right: 0;
    bottom: 12px;
    text-align: center;
    font-size: 10px;
    color: var(--white);
  }

  /* back */
  .back-brand {
    position: absolute;
    left: 42px;
    top: 55px;
  }
  .back-brand .brand-name { font-size: 23px; }

  .back-rule {
    position: absolute;
    left: 32px;
    top: 137px;
    width: 302px;
    height: 1px;
    background: var(--rule);
  }

  .person {
    position: absolute;
    left: 346px;
    top: 94px;
  }
  .person-name { font-size: 27px; font-weight: 700; line-height: 1; }
  .person-role { font-size: 22px; font-weight: 600; line-height: 1.05; }

  .contact-list {
    position: absolute;
    left: 32px;
    top: 160px;
    list-style: none;
    font-size: 15px;
    line-height: 20px;
    color: var(--ink);
  }
  .contact-list li { display: flex; align-items: center; gap: 6px; white-space: nowrap; }
  .contact-icon { width: 12px; height: 12px; flex: none; }

  .address {
    position: absolute;
    left: 346px;
    top: 162px;
    display: flex;
    gap: 8px;
    font-size: 13px;
    line-height: 15px;
  }
  .address .contact-icon { margin-top: 2px; }

  .back-band { position: absolute; left: 0; top: 0; width: 540px; height: 297px; }
</style>
</head>
<body>

  <section class="card card--front" aria-label="Vorderseite">
    <span class="edge-notch edge-notch--left"></span>
    <span class="edge-notch edge-notch--right"></span>
    <div class="front-brand">
      <div class="brand-name">HAUSKLAR.DE</div>
    </div>
    <div class="front-web">www.yourwebsite.com</div>
  </section>

  <section class="card card--back" aria-label="Rückseite">
    <svg class="back-band" viewBox="0 0 540 297" aria-hidden="true">
      <polyline points="0,266 300,266 318,256" fill="none" stroke="var(--teal)" stroke-width="2"/>
      <polygon points="0,280 306,280 330,268 540,268 540,297 0,297" fill="var(--teal)"/>
    </svg>

    <div class="back-brand">
      <div class="brand-name">HAUSKLAR.DE</div>
    </div>

    <div class="back-rule"></div>

    <div class="person">
      <div class="person-name">Your Name</div>
      <div class="person-role">Manager</div>
    </div>

    <ul class="contact-list">
      <li>
        <svg class="contact-icon" viewBox="0 0 12 12" aria-hidden="true">
          <circle cx="6" cy="6" r="6" fill="var(--teal)"/>
          <path d="M4 3.2 5 4.6 4.4 5.3a4 4 0 0 0 2.3 2.3l.7-.6 1.4 1-.6 1.1C5.8 9 3 6.2 2.9 3.8z" fill="var(--white)"/>
        </svg>
        040.555.0187
      </li>
      <li>
        <svg class="contact-icon" viewBox="0 0 12 12" aria-hidden="true">
          <circle cx="6" cy="6" r="6" fill="var(--teal)"/>
          <circle cx="6" cy="6" r="2.6" fill="none" stroke="var(--white)" stroke-width="1.1"/>
        </svg>
        kontakt@hausklar-beispiel.de
      </li>
      <li>
        <svg class="contact-icon" viewBox="0 0 12 12" aria-hidden="true">
          <circle cx="6" cy="6" r="6" fill="var(--teal)"/>
          <path d="M3 4.2 4.3 8 6 5.2 7.7 8 9 4.2" fill="none" stroke="var(--white)" stroke-width="1"/>
        </svg>
        www.hausklar-beispiel.de
      </li>
    </ul>

    <div class="address">
      <svg class="contact-icon" viewBox="0 0 12 12" aria-hidden="true">
        <circle cx="6" cy="6" r="5" fill="none" stroke="var(--teal)" stroke-width="2"/>
      </svg>
      <div>Your addres<br>and number<br>of street</div>
    </div>
  </section>

</body>
</html>
```